Organic Ready Meal/Food Packaging Design

We are looking to re-vamp/re-design our current food packaging. The design will be for an outer box surround for our food which is packed into plastic pots. The meals are fresh and ready to eat. There are 4 variants (recipes) and one design is needed with a background colour change for each recipe. I am looking for a fresh, modern and eye-catching look which stands out on a supermarket shelf. It should be noted that there there is an existing design which needs an overhaul. I would like the winning bidder to look at this together with some other types of packaging I like to improve it.

I have attached a copy of my existing packaging which can also be seen on our company website www.thebrimfieldkitchen.com. We need to move away from this bitty, wishy washy theme to something brighter and bolder, more modern and innovative like the 'Tub o'' example I have also attached. Other points of reference are www.harlowtarts.co.uk and www.figsprout.co.uk which are bright and eye-catching. The Harlow Tarts 'tub o'' boxes are a good benchmark for us although we do not want to copy the design.

This project probably needs to incorporate a modified company logo and the budget can be modified to include this.

We also need to use the word 'Yummy' as a sub-header for our meals i.e.

Yummy
Organic Mediterranean Bean Casserole

Any other questions, please ask at any time.

Target Market(s)

anybody wanting a healthy, organic ready meal
men
women
mums

Industry/Entity Type

It Company

Requirements
Must have
• Bold modern colours/design
Modern eye catching design/fonts
Should not have
• Illustrations (sketchy drawings)

```html
<!DOCTYPE html>
<html lang="en">
<head>
<meta charset="utf-8">
<title>Brimfield Organic Food – Mediterranean Bean Casserole</title>
<link rel="stylesheet" href="https://fonts.googleapis.com/css2?family=Quicksand:wght@500;600&family=Federo&display=swap">
<style>
  :root {
    --backdrop-light: #ffffff;
    --backdrop-shade: #e9e9ea;
    --box-white: #ffffff;
    --lid-grey: #e8e8ea;
    --lid-rim: #c9c9cc;
    --band-pink: #ec66a0;
    --band-pink-text: #f390bb;
    --band-peach: #fdca87;
    --fold-shade: rgba(190, 130, 60, 0.12);
    --ink: #231f20;
    --label-white: #ffffff;
  }

  html, body {
    margin: 0;
    padding: 0;
    overflow: hidden;
  }

  .canvas {
    position: relative;
    width: 1200px;
    height: 720px;
    overflow: hidden;
    background: radial-gradient(ellipse 62% 62% at 50% 48%, var(--backdrop-light) 55%, var(--backdrop-shade) 100%);
  }

  .pack-base {
    position: absolute;
    inset: 0;
  }

  .sleeve-peach {
    position: absolute;
    left: 488px;
    top: 70px;
    width: 224px;
    height: 576px;
    background: var(--band-peach);
    text-align: center;
    color: var(--label-white);
  }

  .sleeve-fold {
    position: absolute;
    left: 0;
    right: 0;
    top: 300px;
    height: 58px;
    background: linear-gradient(to bottom, transparent, var(--fold-shade));
  }

  .brand-name {
    position: absolute;
    left: 0;
    right: 0;
    top: 66px;
    margin: 0;
    font-family: "Quicksand", sans-serif;
    font-weight: 600;
    font-size: 40px;
    line-height: 1;
    color: var(--label-white);
  }

  .range-name {
    position: absolute;
    left: 0;
    right: 0;
    top: 158px;
    margin: 0;
    font-family: "Quicksand", sans-serif;
    font-weight: 500;
    font-size: 41px;
    line-height: 52px;
    color: var(--label-white);
  }

  .divider {
    position: absolute;
    left: 54px;
    width: 116px;
    top: 292px;
    height: 0;
    border-top: 1.5px solid var(--ink);
  }

  .recipe-name {
    position: absolute;
    left: 0;
    right: 0;
    top: 330px;
    margin: 0;
    font-family: "Federo", sans-serif;
    font-size: 30px;
    line-height: 55px;
    color: var(--ink);
  }
</style>
</head>
<body>
  <main class="canvas">
    <svg class="pack-base" width="1200" height="720" viewBox="0 0 1200 720" aria-hidden="true">
      <polygon class="box-top" fill="var(--box-white)"
               points="488,70 712,70 889,248 889,469 712,646 488,646 311,469 311,248"/>
      <circle class="pot-lid" cx="600" cy="358" r="276" fill="var(--lid-grey)" stroke="var(--lid-rim)" stroke-width="2"/>
      <rect class="sleeve-pink" x="311" y="248" width="578" height="221" fill="var(--band-pink)"/>
      <text class="sleeve-pink-title" x="322" y="398" textLength="556" lengthAdjust="spacingAndGlyphs"
            font-family="Federo, sans-serif" font-size="86" fill="var(--band-pink-text)">Mediterranean Bean Casserole</text>
    </svg>

    <section class="sleeve-peach">
      <div class="sleeve-fold"></div>
      <h1 class="brand-name">Brimfield</h1>
      <p class="range-name">Organic<br>Food</p>
      <div class="divider"></div>
      <h2 class="recipe-name">Mediterranean<br>Bean Casserole</h2>
    </section>
  </main>
</body>
</html>
```